tavrenimports.com

I had a logo designed by pixel harbor, and now need a website. I would like all the normal features a website would need.
Payment method etc and I'd like to be able to upload pictures

Target Market(s)

Parents, gift ideas, baby shower, online shopping

Industry/Entity Type

Crowd

Coding

Coded - Design and coding required

Number of Pages Required

1 page

Requirements
Must have
• Would like it to be accessible using a mobile phone
• must be given DNS code so i can add pages as needed
• must be able to upload pictures of products, and up date as needed
Nice to have
• additional pages with no content

```html
<!DOCTYPE html>
<html lang="en">
<head>
<meta charset="utf-8">
<title>Tavren – Online Baby Store</title>
<link rel="stylesheet" href="https://fonts.googleapis.com/css2?family=Questrial&family=Asap:wght@400;700&family=Sacramento&family=Open+Sans:wght@400;600&display=swap">
<style>
:root{
  --sand:#f7d9a6;
  --cream:#fbf0d4;
  --white:#ffffff;
  --ink:#222831;
  --grey:#6b6b6b;
  --grey-light:#a9a9a9;
  --pink:#f4a0c4;
  --pink-deep:#f08fa0;
  --rose:#ef8c9a;
  --blue:#8fcfe0;
  --teal:#1fd1c4;
  --tag:#8aa9a6;
  --gold:#f3c777;
  --card-pink:#fbeff6;
}
*{box-sizing:border-box;margin:0;padding:0}
html,body{width:1200px;height:2305px;overflow:hidden}
body{position:relative;background:var(--white);font-family:"Questrial",sans-serif;color:var(--ink)}
.abs{position:absolute}

/* header */
.site-header{position:absolute;left:0;top:0;width:1200px;height:97px;background:var(--white)}
.brand{position:absolute;left:88px;top:28px;display:flex;align-items:center;gap:10px;font-family:"Questrial",sans-serif;font-size:44px;color:#2d3f7a;line-height:1}
.brand-dot{width:16px;height:16px;border-radius:50%;background:var(--pink)}
.search{position:absolute;left:380px;top:41px;width:230px;height:27px;border-radius:14px;background:#efefef;font-size:10px;color:#aaa;letter-spacing:1px;padding:8px 12px}
.search-btn{position:absolute;right:0;top:0;width:27px;height:27px;border-radius:50%;background:var(--sand)}
.util{position:absolute;top:48px;font-size:11px;letter-spacing:1px;color:var(--ink)}
.basket{position:absolute;left:979px;top:44px;display:flex;gap:8px;align-items:center;font-size:11px;letter-spacing:1px}

/* nav */
.main-nav{position:absolute;left:0;top:97px;width:1200px;height:52px;background:var(--sand)}
.main-nav a{position:absolute;top:13px;color:var(--white);text-decoration:none;font-size:22px;letter-spacing:2px}

/* hero */
.hero{position:absolute;left:0;top:149px;width:1200px;height:374px;background:var(--white);overflow:hidden}
.cloud{position:absolute;border-radius:40px}
.hero-kicker{position:absolute;left:227px;top:148px;font-size:17px;letter-spacing:1px;color:var(--gold)}
.hero-title{position:absolute;left:227px;top:170px;font-family:"Asap",sans-serif;font-weight:700;font-size:31px;line-height:37px;color:var(--grey)}
.hero-title em{font-style:normal;color:var(--pink)}
.hero-btn{position:absolute;left:224px;top:289px;width:118px;height:30px;border-radius:15px;background:var(--pink);color:var(--white);font-size:14px;letter-spacing:1px;padding:7px 0 0 16px}

/* promo */
.cream{position:absolute;left:0;top:523px;width:1200px;height:1275px;background:var(--cream)}
.promo{position:absolute;top:536px;width:266px;height:378px;background:var(--white);overflow:hidden;text-align:center}
.promo-script{font-family:"Sacramento",cursive;font-size:28px;margin-top:28px;line-height:32px}
.promo-sale{font-size:23px;letter-spacing:2px;color:var(--grey);margin-top:4px}
.age{display:inline-block;margin-top:12px;padding:3px 8px;font-size:11px;color:var(--white);letter-spacing:1px}
.promo-arc{position:absolute;left:-30px;bottom:-150px;width:326px;height:300px;border-radius:50%}
.deal{position:absolute;left:467px;top:728px;width:266px;height:180px;background:var(--teal);text-align:center;color:var(--white)}

/* collection */
.collection{position:absolute;left:186px;top:928px;width:825px;height:493px;background:var(--white)}
.collection-title{position:absolute;top:42px;width:100%;text-align:center;font-size:23px;letter-spacing:3px;color:var(--grey)}
.tabs{position:absolute;top:77px;left:0;width:100%;display:flex;justify-content:center;gap:30px;font-size:14px;letter-spacing:2px;color:var(--grey)}
.tabs span{padding:10px 10px}
.tabs .active{background:var(--pink);color:var(--white);border-radius:20px;padding:10px 18px}
.product{position:absolute;top:154px;width:194px;height:286px;border:1px solid #999;overflow:hidden;text-align:center;background:var(--white)}
.product-photo{position:absolute;left:30px;top:22px;width:134px;height:150px;border-radius:8px}
.product-arc{position:absolute;left:-10px;top:192px;width:214px;height:200px;border-radius:50%;background:var(--card-pink)}
.product-name{position:absolute;top:226px;width:100%;font-size:14px;letter-spacing:2px;font-weight:700;font-family:"Asap",sans-serif}
.stars{position:absolute;top:243px;width:100%;font-size:10px;color:var(--gold)}
.product-line{position:absolute;left:25px;right:25px;top:258px;border-top:1px solid #ddd}
.price{position:absolute;top:264px;width:100%;font-size:13px;font-family:"Asap",sans-serif}
.tag{position:absolute;left:2px;top:-2px;width:46px;height:52px;background:var(--tag);color:var(--white);font-size:10px;line-height:11px;padding-top:6px;clip-path:polygon(0 0,100% 0,100% 100%,50% 80%,0 100%)}
.pager{position:absolute;top:460px;left:386px;display:flex;gap:10px}

/* newsletter */
.newsletter{position:absolute;left:187px;top:1435px;width:825px;height:155px;background:var(--pink-deep)}
.newsletter-frame{position:absolute;inset:8px;border:1px solid rgba(255,255,255,.8)}
.newsletter-title{position:absolute;left:78px;top:42px;font-family:"Sacramento",cursive;font-size:46px;color:var(--white)}
.newsletter-sub{position:absolute;left:42px;top:88px;font-size:14px;color:var(--white)}
.email{position:absolute;left:312px;top:63px;width:215px;height:28px;background:var(--white);font-size:10px;color:#aaa;padding:8px}
.subscribe{position:absolute;left:529px;top:63px;width:108px;height:28px;background:var(--sand);color:var(--white);font-size:10px;letter-spacing:1px;padding:8px 0 0 32px}

/* features */
.feature{position:absolute;top:1621px;width:200px;text-align:center}
.feature svg{display:block;margin:0 auto}
.feature-title{margin-top:12px;font-family:"Asap",sans-serif;font-size:18px;color:var(--ink)}
.feature-sub{font-family:"Asap",sans-serif;font-size:11px;font-weight:700;color:var(--ink)}

/* footer */
.site-footer{position:absolute;left:0;top:1798px;width:1200px;height:395px;background:var(--white)}
.footer-brand{position:absolute;left:186px;top:48px;display:flex;align-items:center;gap:8px;font-size:38px;color:#2d3f7a}
.footer-about{position:absolute;left:186px;top:100px;width:330px;font-family:"Open Sans",sans-serif;font-size:13px;line-height:19px;color:var(--grey)}
.contact{position:absolute;left:186px;font-family:"Open Sans",sans-serif;font-size:13px;color:var(--grey);display:flex;gap:4px;align-items:center}
.col-title{position:absolute;top:86px;font-family:"Asap",sans-serif;font-weight:700;font-size:12px;letter-spacing:1px}
.col-link{position:absolute;font-family:"Open Sans",sans-serif;font-size:12px;letter-spacing:1px;color:var(--grey)}
.insta{position:absolute;width:55px;height:55px}
.footer-rule{position:absolute;left:0;top:299px;width:1200px;border-top:1px solid #ccc}
.social{position:absolute;top:332px;width:37px;height:37px;border-radius:50%;background:#d3d3d3}
.bottom-band{position:absolute;left:0;top:2193px;width:1200px;height:112px;background:var(--sand)}
.copyright{position:absolute;top:40px;width:100%;text-align:center;font-family:"Open Sans",sans-serif;font-size:17px;letter-spacing:2px;color:var(--white)}
</style>
</head>
<body>

<header class="site-header">
  <div class="brand">Tavren<span class="brand-dot"></span></div>
  <div class="search">SEARCH<span class="search-btn"></span></div>
  <span class="util" style="left:654px">MY ACCOUNT ⌄</span>
  <span class="util" style="left:760px">LANGUAGES ⌄</span>
  <span class="util" style="left:862px">CURRENCY ⌄</span>
  <div class="basket">
    <svg width="18" height="16" viewBox="0 0 18 16"><path d="M1 5h16l-2 10H3z" fill="#8fcfe0"/><path d="M5 5a4 4 0 0 1 8 0" fill="none" stroke="#8fcfe0" stroke-width="1.5"/></svg>
    0 ITEMS BASKET
  </div>
</header>

<nav class="main-nav">
  <a style="left:210px">HOME</a>
  <a style="left:322px">CATEGORIES</a>
  <a style="left:506px">BOYS</a>
  <a style="left:610px">GIRLS</a>
  <a style="left:720px">DEALS</a>
  <a style="left:836px">BLOG</a>
  <a style="left:942px">FAQ</a>
</nav>

<section class="hero">
  <div class="cloud" role="img" aria-label="Blue swirl cloud" style="left:80px;top:0;width:140px;height:80px;background:#8ecde0"></div>
  <div class="cloud" role="img" aria-label="Turquoise cloud" style="left:248px;top:36px;width:122px;height:66px;background:var(--teal)"></div>
  <div class="cloud" role="img" aria-label="Pink star cloud" style="left:4px;top:88px;width:88px;height:58px;background:#f08a9c"></div>
  <div class="cloud" role="img" aria-label="Pink star cloud" style="left:988px;top:0;width:120px;height:62px;background:#f08a9c"></div>
  <div class="cloud" role="img" aria-label="Turquoise cloud" style="left:1114px;top:52px;width:90px;height:64px;background:var(--teal)"></div>
  <svg class="abs" style="left:600px;top:112px" width="600" height="262"><path d="M0 262A300 300 0 0 1 600 262Z" fill="#f4a7c8"/></svg>
  <div class="abs" role="img" aria-label="Baby wearing a toy crown" style="left:722px;top:28px;width:430px;height:346px;border-radius:180px 180px 0 0;background:linear-gradient(180deg,#e8d4c4,#e9c3a8 55%,#9fc4d4)"></div>
  <div class="hero-kicker">ONLINE SHOPPING STORE</div>
  <h1 class="hero-title">From <em>must have</em> basic<br>to fancy looks,<br>we’ve got it all</h1>
  <div class="hero-btn">SHOP NOW 〉</div>
</section>

<div class="cream"></div>

<section class="promo" style="left:187px">
  <div class="promo-script" style="color:#7cc0d8">Boys collections</div>
  <div class="promo-sale">UP TO 50% SALE</div>
  <span class="age" style="background:var(--blue)">0–5 YEARS</span>
  <div class="promo-arc" style="background:#a6d8ea"></div>
  <div class="abs" role="img" aria-label="Mint baby bodysuit" style="left:50px;top:148px;width:166px;height:214px;border-radius:20px;background:#8fd3c3"></div>
</section>

<div class="abs" role="img" aria-label="Knit baby trousers and shoes flat lay" style="left:467px;top:536px;width:266px;height:182px;background:linear-gradient(135deg,#f2f0ec,#d9d6d0)"></div>
<section class="deal">
  <svg class="abs" style="left:110px;top:30px" width="46" height="52"><circle cx="23" cy="22" r="21" fill="#c9d6d6"/><circle cx="23" cy="22" r="14" fill="#7a9aa0"/><path d="M12 40l-4 10 8-3 7 5 7-5 8 3-4-10z" fill="#ef8c9a"/></svg>
  <div class="abs" style="top:94px;width:100%;font-size:23px;letter-spacing:2px">UP TO 50% SALE</div>
  <div class="abs" style="top:134px;width:100%;font-size:17px;letter-spacing:1px">FREE SHIPPING</div>
  <div class="abs" style="top:154px;width:100%;font-size:10px;letter-spacing:1px">ON ORDER OF 100 EURO</div>
</section>

<section class="promo" style="left:745px">
  <div class="promo-script" style="color:var(--rose)">Girls collection</div>
  <div class="promo-sale">UP TO 50% SALE</div>
  <span class="age" style="background:var(--rose)">0–5 YEARS</span>
  <div class="promo-arc" style="background:#ef8c9a"></div>
  <div class="abs" role="img" aria-label="Girl in red skirt and cardigan" style="left:78px;top:142px;width:110px;height:220px;border-radius:40px;background:linear-gradient(180deg,#c9a48a,#d23a3a 55%,#7a5646)"></div>
</section>

<section class="collection">
  <h2 class="collection-title">NEW COLLECTION</h2>
  <div class="tabs"><span class="active">SALE</span><span>FEATURE</span><span>BESTSELLER</span><span>SPECIAL</span></div>

  <div class="product" style="left:9px">
    <div class="product-photo" role="img" aria-label="Pink baby sandals" style="background:#f2c9c4"></div>
    <div class="product-arc"></div>
    <div class="tag">BEST<br>SALE<br>★</div>
    <div class="product-name">SANDALS</div><div class="stars">★★★</div><div class="product-line"></div><div class="price">13.00£</div>
  </div>
  <div class="product" style="left:214px">
    <div class="product-photo" role="img" aria-label="Denim bodysuit with brown trousers" style="background:linear-gradient(180deg,#8ea2b6,#a87a3e)"></div>
    <div class="product-arc"></div>
    <div class="product-name">KIT</div><div class="stars">★★★</div><div class="product-line"></div><div class="price">48.00£</div>
  </div>
  <div class="product" style="left:419px">
    <div class="product-photo" role="img" aria-label="Mint coat with fur collar" style="background:#c7d6d3"></div>
    <div class="product-arc"></div>
    <div class="tag">BEST<br>SALE<br>★</div>
    <div class="product-name">JACKET</div><div class="stars">★★★</div><div class="product-line"></div><div class="price">70.00£</div>
  </div>
  <div class="product" style="left:623px">
    <div class="product-photo" role="img" aria-label="Dark grey printed baby bodysuit" style="background:#3c3e48"></div>
    <div class="product-arc"></div>
    <div class="product-name">BODY</div><div class="stars">★★★</div><div class="product-line"></div><div class="price">9.00£</div>
  </div>

  <div class="pager">
    <svg width="22" height="14"><path d="M21 7H2M8 1L2 7l6 6" fill="none" stroke="#999" stroke-width="1.5"/></svg>
    <svg width="22" height="14"><path d="M1 7h19M14 1l6 6-6 6" fill="none" stroke="#999" stroke-width="1.5"/></svg>
  </div>
</section>

<section class="newsletter">
  <div class="newsletter-frame"></div>
  <div class="newsletter-title">Newsletter</div>
  <div class="newsletter-sub">and you get your 25% discount now!</div>
  <div class="email">YOUR EMAIL</div>
  <div class="subscribe">✉ SUBSCRIBE</div>
  <div class="abs" role="img" aria-label="Smiling baby in orange shirt" style="left:688px;top:14px;width:106px;height:141px;border-radius:50px 50px 0 0;background:linear-gradient(180deg,#f1d3bf,#f2b45a)"></div>
</section>

<div class="feature" style="left:150px">
  <svg width="62" height="62" viewBox="0 0 62 62" fill="none" stroke="#222" stroke-width="2"><path d="M31 3l24 8v18c0 16-11 26-24 30C18 55 7 45 7 29V11z"/><path d="M21 31l7 7 14-15"/></svg>
  <div class="feature-title">GUARANTEES</div><div class="feature-sub">RETURN WITHIN 14 DAYS</div>
</div>
<div class="feature" style="left:375px">
  <svg width="62" height="62" viewBox="0 0 62 62" fill="none" stroke="#222" stroke-width="2"><rect x="4" y="22" width="32" height="24"/><path d="M36 30h12l8 9v7H36z"/><circle cx="15" cy="49" r="5"/><circle cx="46" cy="49" r="5"/><circle cx="20" cy="12" r="8"/><path d="M20 8v4h3"/></svg>
  <div class="feature-title">DELIVERY</div><div class="feature-sub">3 SHIPPING METHODS</div>
</div>
<div class="feature" style="left:607px">
  <svg width="62" height="62" viewBox="0 0 62 62" fill="none" stroke="#222" stroke-width="2"><rect x="8" y="22" width="46" height="12"/><rect x="12" y="34" width="38" height="24"/><path d="M31 22v36M31 22c-8-12-18-8-12-2zM31 22c8-12 18-8 12-2z"/></svg>
  <div class="feature-title">PAYMENTS</div><div class="feature-sub">CASH AND NON-CASH</div>
</div>
<div class="feature" style="left:830px">
  <svg width="62" height="62" viewBox="0 0 62 62" fill="none" stroke="#222" stroke-width="2"><path d="M56 31A25 25 0 1 1 46 11"/><path d="M46 4v7h7"/><text x="17" y="36" font-size="18" font-family="Asap" fill="#222" stroke="none">24</text><text x="35" y="46" font-size="7" font-family="Asap" fill="#222" stroke="none">HR</text></svg>
  <div class="feature-title">CONTACT</div><div class="feature-sub">24H SERVICE</div>
</div>

<footer class="site-footer">
  <div class="footer-brand">Tavren<span class="brand-dot"></span></div>
  <p class="footer-about">Lorem ipsum dolor sit amet, consectetur adipiscing elit, sed do eiusmod tempor incididunt ut labore et dolore magna aliqua</p>
  <div class="contact" style="top:162px"><svg width="12" height="14"><path d="M6 13C2 8 1 6 1 5a5 5 0 0 1 10 0c0 1-1 3-5 8z" fill="none" stroke="#888"/><circle cx="6" cy="5" r="2" fill="#888"/></svg>14 marlow lane ashford</div>
  <div class="contact" style="top:192px"><svg width="12" height="14"><path d="M2 1l3 0 1 3-2 2c1 2 2 3 4 4l2-2 3 1v3c-6 0-11-5-11-11z" fill="none" stroke="#888"/></svg>tel 00044 210 55 93</div>
  <div class="contact" style="top:220px"><svg width="12" height="10"><rect x=".5" y=".5" width="11" height="9" fill="none" stroke="#888"/><path d="M1 1l5 4 5-4" fill="none" stroke="#888"/></svg>hello@tavrenimports.com</div>

  <div class="col-title" style="left:541px">INFORMATION</div>
  <span class="col-link" style="left:541px;top:110px">about us</span>
  <span class="col-link" style="left:541px;top:137px">delivery information</span>
  <span class="col-link" style="left:541px;top:165px">privacy policy</span>
  <span class="col-link" style="left:541px;top:191px">terms &amp; conditions</span>

  <div class="col-title" style="left:702px">INSTAGRAM</div>
  <div class="insta" role="img" aria-label="Baby in knit hat" style="left:700px;top:107px;background:#5f5f66"></div>
  <div class="insta" role="img" aria-label="White baby outfit" style="left:765px;top:107px;background:#dcdcdc"></div>
  <div class="insta" role="img" aria-label="Teddy bears" style="left:828px;top:107px;background:#a57a5a"></div>
  <div class="insta" role="img" aria-label="Child in navy coat" style="left:700px;top:172px;background:#3f4f6e"></div>
  <div class="insta" role="img" aria-label="Pink floral fabric" style="left:765px;top:172px;background:#d78aa6"></div>
  <div class="insta" role="img" aria-label="Twin toddlers" style="left:828px;top:172px;background:#c9b6b4"></div>

  <div class="col-title" style="left:919px">MY ACCOUNT</div>
  <span class="col-link" style="left:919px;top:108px">my account</span>
  <span class="col-link" style="left:919px;top:135px">wishlist</span>
  <span class="col-link" style="left:919px;top:163px">order history</span>
  <span class="col-link" style="left:919px;top:190px">site maps</span>
  <span class="col-link" style="left:919px;top:217px">returns</span>

  <div class="footer-rule"></div>
  <span class="social" style="left:520px" aria-label="Social link"></span>
  <span class="social" style="left:561px" aria-label="Social link"></span>
  <span class="social" style="left:603px" aria-label="Social link"></span>
  <span class="social" style="left:643px" aria-label="Social link"></span>
</footer>

<div class="bottom-band">
  <div class="copyright">copyright 2017 | All right reserved</div>
</div>

</body>
</html>
```